Subway/Bus ad sign for a paid research study

We are looking for someone who can help design an effective advertisement sign for a paid research study. The ad will be displayed in subway stations/bus. The study involves fMRI and is conducted by a laboratory in the Calder Valley University.

We prefer ppt images so we could edit. Dimensions should be 46”h x 60”w, but may vary in the final version depending on our needs.

The way we would like to choose the final design is by running a pretest on plumfeed to pick the most attractive ad. Your submission would mean that you consent with this process.

Thank you for your consideration.

Target Market(s)

age 18-64, philadelphia

Requirements
Must have
• The ad must include the following information (we encourage you to come up with better/more catchy slogans)
• - We are looking for participants for a research study
• - This fMRI study is conducted by researchers at Calder Valley University
• - Email CvuCV2@lab.cvu-mail.org to see if you are eligible
• - Calder Valley University Logo
• The ad may include the following information
• - Participants get paid up to $190
Nice to have
• original attractive illustrations are highly encouraged.
Should not have
• It seems like brain photos tend to scare people away. Maybe you could focus on using survey-related images or illustrated images of the brain (vs. fMRI scans).

```html
<!DOCTYPE html>
<html lang="en">
<head>
<meta charset="utf-8">
<title>fMRI Research Study – Calder Valley University</title>
<link href="https://fonts.googleapis.com/css2?family=Archivo+Black&family=Arimo:ital,wght@0,400;0,700;1,400;1,700&display=swap" rel="stylesheet">
<style>
  :root {
    --navy: #1f2a63;
    --red: #a81c22;
    --white: #ffffff;
    --mist: #f7f7f7;
    --shade: #a9a9ab;
  }
  * { margin: 0; padding: 0; box-sizing: border-box; }
  html, body { width: 1200px; height: 920px; overflow: hidden; background: var(--white); }
  .poster {
    position: relative; width: 1200px; height: 920px;
    font-family: "Arimo", Arial, sans-serif;
  }
  .headline-band {
    height: 95px; background: var(--navy);
    display: flex; align-items: center; justify-content: center;
  }
  .headline {
    font-family: "Archivo Black", "Arial Black", sans-serif;
    color: var(--white); font-size: 60px; letter-spacing: 1px; line-height: 1;
  }
  .stage {
    position: relative; height: 675px;
    background: radial-gradient(ellipse 62% 70% at 50% 50%, var(--white) 35%, var(--mist) 55%, var(--shade) 100%);
  }
  .subhead {
    position: absolute; top: 26px; width: 100%; text-align: center;
    color: var(--red); font-weight: 700; font-size: 50px;
  }
  .brain-art {
    position: absolute; left: 360px; top: 110px; width: 475px; height: 380px;
    border-radius: 48% 52% 44% 50% / 50% 48% 56% 50%;
    background: linear-gradient(120deg, #3aa13c 0%, #f0a31c 22%, #e8303e 45%, #d5258f 62%, #8e9aa6 78%, #2b3b9b 100%);
    opacity: 0.9;
  }
  .payment {
    position: absolute; top: 515px; width: 100%; text-align: center;
    color: var(--red); font-weight: 700; font-size: 44px;
  }
  .contact {
    position: absolute; top: 620px; width: 100%; text-align: center;
    color: var(--navy); font-style: italic; font-size: 29px;
  }
  .contact strong { font-weight: 700; }
  .footer { display: flex; height: 150px; }
  .credit {
    width: 600px; background: var(--navy); color: var(--white);
    display: flex; align-items: center; justify-content: center;
    text-align: center; font-weight: 700; font-size: 26px; line-height: 1.25;
  }
  .sponsor {
    width: 600px; background: var(--white);
    display: flex; align-items: center; justify-content: center; gap: 22px;
  }
  .sponsor-mark { width: 70px; height: 70px; background: var(--navy); }
  .sponsor-name {
    color: var(--navy); font-weight: 700; font-size: 40px; line-height: 1.05;
  }
</style>
</head>
<body>
<main class="poster">
  <header class="headline-band">
    <h1 class="headline">We Need Your Brain...</h1>
  </header>
  <section class="stage">
    <p class="subhead">...for an fMRI research study.</p>
    <div class="brain-art" role="img" aria-label="Colourful mosaic illustration of a brain in side view"></div>
    <p class="payment">Participants get paid up to $190</p>
    <p class="contact">Email <strong>CvuCV2@lab.cvu-mail.org</strong> to see if you are eligible</p>
  </section>
  <footer class="footer">
    <p class="credit">This fMRI study is conducted<br>by researchers at<br>Calder Valley University</p>
    <div class="sponsor">
      <span class="sponsor-mark"></span>
      <span class="sponsor-name">Calder Valley<br>University</span>
    </div>
  </footer>
</main>
</body>
</html>
```